Brill's Jewelers website (www.brillsjewelers-example.com)

We are in need of a web storefront for a retail Jewelry store.
www.brillsjewelers-example.com
https://www.facebook.com/Brills-Jewelers-Palm-Vista-740315928461257/

Brill's Jewelers is located in Coral Gables, Florida. The store has been family owned and operated since 1958. Their focus customers are high-income families that care about quality over the brand name. They mostly sell fashion jewelry and diamonds up to 8 carats. We are looking for a simple minimalistic site that their customers can view their inventory and purchase items online.

Competitors websites:
https://www.orvinjewelers-example.com/
http://www.pelvaro-example.com/
http://truecutjewelers-example.com/

Pages:
-Home (with message bulletin)
-Jewelry
We would be able to create the subpages ie Rings, Bracelets, Earrings, Necklaces, Estate, Watches, Men's, Children's
-Services
We would need sub pages ie Appraisals, Consignment, Repairs
-About us
-Contact

Target Market(s)

Local wealthy families

Coding

Number of Pages Required

Font styles to use
Serif

Requirements
Must have
• -An E-commerce site customers can buy jewelry online.
-An easy process internally to add new items to the site
-Colors are Black and White or Black and Gold
Nice to have
• I would like to stay away from face shots of random models in stock photos. I want the jewelry pieces as the focus, not models.

```html
<!DOCTYPE html>
<html lang="en">
<head>
<meta charset="utf-8">
<title>Brill's Jewelers — Our Jewelry</title>
<link rel="stylesheet" href="https://fonts.googleapis.com/css2?family=Libre+Baskerville:wght@400;700&family=Poppins:wght@300;400;500;600&display=swap">
<style>
:root{
  --gold:#d8ac2c;
  --black:#000;
  --ink:#222;
  --muted:#555;
  --line:#e2e2e2;
  --band:#f3f3f3;
  --white:#fff;
  --star:#dcdcdc;
}
*{box-sizing:border-box;margin:0;padding:0}
html,body{width:1200px;height:2867px;overflow:hidden;background:var(--white)}
body{position:relative;font-family:"Poppins",sans-serif;color:var(--ink)}
a{color:inherit;text-decoration:none}

/* top bar */
.topbar{position:absolute;left:0;top:0;width:1200px;height:39px;border-bottom:1px solid var(--line);font-size:13px}
.topbar .note{position:absolute;left:87px;top:11px}
.topbar .links{position:absolute;right:88px;top:11px;display:flex;font-size:12.5px}
.topbar .links span{display:flex;align-items:center;gap:5px;padding:0 16px;border-left:1px solid var(--line)}
.topbar .links span:first-child{border-left:0}
.topbar svg{width:14px;height:14px}

/* nav */
.nav{position:absolute;top:39px;left:0;width:1200px;height:115px}
.nav a{position:absolute;top:52px;font-size:14px;font-weight:500;letter-spacing:.2px}
.nav a.current{color:var(--gold)}
.brand{position:absolute;left:450px;top:42px;width:300px;text-align:center;font-family:"Libre Baskerville",serif;font-weight:700;font-size:26px;line-height:34px;color:var(--black)}
.nav .search{position:absolute;left:1098px;top:53px;width:14px;height:14px}

/* page header */
.pagehead{position:absolute;top:154px;left:0;width:1200px;height:124px;background:var(--band)}
.pagehead h1{position:absolute;left:89px;top:36px;font-family:"Libre Baskerville",serif;font-size:46px;font-weight:700;letter-spacing:1px;color:var(--black)}
.crumbs{position:absolute;right:100px;top:50px;font-size:16px;display:flex;gap:12px;align-items:center}
.crumbs .here{color:var(--gold)}

/* sidebar */
.side{position:absolute;left:89px;width:223px}
.side h3{font-size:15px;font-weight:600;letter-spacing:.3px;padding-bottom:8px;border-bottom:1px solid var(--line);color:var(--black)}
.side ul{list-style:none}
.side li{height:31px;display:flex;align-items:center;font-size:14.5px;color:var(--muted);justify-content:space-between}
.side li .plus{color:var(--gold);font-size:12px;margin-right:4px}
.side li .box{display:inline-block;width:14px;height:14px;border:1px solid #c9c9c9;margin-right:6px;vertical-align:-2px}
.side li .count{font-size:13.5px}
.searchbox{display:flex;height:44px;border:1px solid #cfcfcf;margin-top:6px}
.searchbox span{flex:1;font-size:11.5px;color:#999;padding:14px 8px}
.searchbox i{width:44px;border-left:1px solid #cfcfcf;display:flex;align-items:center;justify-content:center}
.swatches{display:flex;gap:2px;margin-top:14px}
.swatches span{width:33px;height:33px;border-radius:50%}
.tags{margin-top:18px;width:223px}
.tagrow{display:flex;gap:3px;margin-bottom:6px}
.tagrow span{height:30px;border:1px solid #cfcfcf;font-size:10px;font-weight:600;display:flex;align-items:center;padding:0 11px;color:#222}

/* toolbar */
.toolbar{position:absolute;left:367px;top:385px;width:745px;height:44px;font-size:14.5px;color:#333}
.toolbar .views{position:absolute;left:0;top:12px;display:flex;gap:10px}
.toolbar .count{position:absolute;left:80px;top:11px}
.toolbar .sortlabel{position:absolute;left:458px;top:11px}
.select{position:absolute;left:523px;top:0;width:222px;height:44px;border:1px solid #cfcfcf;display:flex}
.select span{flex:1;padding:12px;font-size:14px;color:#aaa}
.select i{width:44px;border-left:1px solid #cfcfcf;display:flex;align-items:center;justify-content:center}

/* products */
.grid{position:absolute;left:367px;top:461px;width:745px;display:grid;grid-template-columns:repeat(3,237px);column-gap:17px;row-gap:17px}
.card{height:330px;border:1px solid #ececec;position:relative;text-align:center;overflow:hidden}
.card .photo{position:absolute;left:18px;top:18px;right:18px;height:190px;border-radius:4px}
.card .stars{position:absolute;left:0;right:0;top:232px;display:flex;justify-content:center;gap:5px}
.card .stars svg{width:13px;height:13px;fill:var(--star)}
.card h4{position:absolute;left:0;right:0;top:260px;font-family:"Libre Baskerville",serif;font-size:15.5px;font-weight:700;color:var(--black);letter-spacing:.3px}
.card .price{position:absolute;left:0;right:0;top:283px;font-size:22px;font-weight:600;color:var(--gold)}
.card.is-active .stars{top:206px}
.card.is-active h4{top:234px}
.card.is-active .price{top:256px}
.card .actions{position:absolute;left:0;right:0;bottom:0;height:34px;display:flex;gap:2px}
.card .actions .add{width:130px;background:var(--gold);color:var(--white);font-size:13.5px;font-weight:500;display:flex;align-items:center;justify-content:center}
.card .actions .ic{flex:1;background:var(--black);display:flex;align-items:center;justify-content:center}
.card .actions svg{width:13px;height:13px}

.gold-photo{background:radial-gradient(circle at 50% 50%,#f2d27a 0,#d9ac3a 45%,#fff 70%)}
.mixed-photo{background:radial-gradient(ellipse at 50% 50%,#c9a266 0,#d8cfc2 45%,#fff 72%)}
.silver-photo{background:radial-gradient(ellipse at 50% 50%,#e9ecef 0,#b9bec4 40%,#fff 72%)}
.pearl-photo{background:radial-gradient(ellipse at 50% 50%,#f5f3ea 0,#d8d6cc 42%,#fff 72%)}
.color-photo{background:radial-gradient(ellipse at 50% 50%,#e36b7d 0,#4fb3c4 35%,#f3d04a 50%,#fff 72%)}

/* pagination */
.pager{position:absolute;top:2211px;left:0;width:1200px;height:31px;font-size:14px}
.pager .prev{position:absolute;left:571px;width:77px;height:31px;background:#eeeeee;display:flex;align-items:center;justify-content:center;color:#444}
.pager .num{position:absolute;top:6px}
.pager .on{position:absolute;left:695px;top:0;width:31px;height:31px;border-radius:50%;background:var(--gold);display:flex;align-items:center;justify-content:center}
.pager .next{position:absolute;left:830px;width:77px;height:31px;background:var(--black);color:var(--white);display:flex;align-items:center;justify-content:center;font-weight:500}

/* footer */
.footer{position:absolute;left:0;top:2330px;width:1200px;height:537px;background:var(--black);color:var(--white)}
.footer h2{position:absolute;left:0;right:0;top:52px;text-align:center;font-family:"Libre Baskerville",serif;font-size:40px;font-weight:700;letter-spacing:1px}
.signup{position:absolute;left:278px;top:106px;width:644px;height:61px;background:var(--white);display:flex;align-items:center;padding:4px}
.signup .field{flex:1;display:flex;align-items:center;gap:10px;padding-left:20px;font-size:16px;color:#777}
.signup .btn{width:145px;height:53px;background:var(--gold);color:var(--white);display:flex;align-items:center;justify-content:center;font-weight:600;font-size:15px;letter-spacing:.5px}
.fbrand{position:absolute;left:89px;top:283px;width:245px;text-align:center;font-family:"Libre Baskerville",serif;font-weight:700;font-size:25px;line-height:34px;white-space:nowrap}
.social{position:absolute;left:145px;top:347px;display:flex;gap:8px}
.social span{width:37px;height:37px;border-radius:50%}
.fcol{position:absolute;top:230px}
.fcol h5{font-size:18px;font-weight:500;color:#666;margin-bottom:18px}
.fcol p{font-size:14px;line-height:27px;color:var(--white)}
.contact p{display:flex;gap:14px;align-items:flex-start;margin-bottom:12px;line-height:19px;font-size:14.5px}
.contact svg{width:13px;height:13px;margin-top:3px;flex:none}
.contact .mail{font-size:12.5px;white-space:nowrap}
.fline{position:absolute;left:89px;top:470px;width:1022px;border-top:1px solid #222}
.copy{position:absolute;left:0;right:0;top:495px;text-align:center;font-size:14px}
.pay{position:absolute;left:968px;top:488px;display:flex;gap:5px}
.pay span{width:44px;height:28px;border-radius:3px;background:#f1f1f1}
.pay span:nth-child(2){background:#1a4fd6}
.chat{position:absolute;left:1130px;top:2779px;width:40px;height:40px;border-radius:50%;background:var(--white);display:flex;align-items:center;justify-content:center}
</style>
</head>
<body>

<header class="topbar">
  <div class="note">Free nationwide shipping or curbside pickup while our store is temporarily closed</div>
  <div class="links">
    <span><svg viewBox="0 0 24 24"><path d="M3 4h3l2 11h11l2-8H7" fill="none" stroke="#000" stroke-width="2.5"/><circle cx="9" cy="20" r="1.8"/><circle cx="18" cy="20" r="1.8"/></svg>CART</span>
    <span><svg viewBox="0 0 24 24"><path d="M12 21l-8-8a5 5 0 017-7l1 1 1-1a5 5 0 017 7z"/></svg>WISHLIST</span>
    <span><svg viewBox="0 0 24 24"><circle cx="12" cy="7" r="5"/><path d="M3 23c0-6 4-9 9-9s9 3 9 9z"/></svg>LOGIN</span>
  </div>
</header>

<nav class="nav">
  <a style="left:159px">HOME</a>
  <a style="left:234px">ABOUT US</a>
  <a class="current" style="left:339px">OUR JEWELRY</a>
  <div class="brand">Brill's Jewelers</div>
  <a style="left:761px">DIAMONDS</a>
  <a style="left:872px">SERVICES</a>
  <a style="left:972px">CONTACT</a>
  <svg class="search" viewBox="0 0 24 24"><circle cx="10" cy="10" r="7" fill="none" stroke="#000" stroke-width="3"/><path d="M15 15l7 7" stroke="#000" stroke-width="3"/></svg>
</nav>

<section class="pagehead">
  <h1>OUR JEWELRY</h1>
  <div class="crumbs"><span><svg width="15" height="13" viewBox="0 0 24 20"><path d="M12 0L0 10h3v10h7v-6h4v6h7V10h3z" fill="#bbb"/></svg> Home</span><span>|</span><span class="here">Jewelry</span></div>
</section>

<aside>
  <div class="side" style="top:362px">
    <h3 style="border:0;padding:0">SEARCH</h3>
    <div class="searchbox"><span>Search Our Store</span><i><svg width="17" height="17" viewBox="0 0 24 24"><circle cx="10" cy="10" r="7" fill="none" stroke="#000" stroke-width="3"/><path d="M15 15l7 7" stroke="#000" stroke-width="3"/></svg></i></div>
  </div>

  <div class="side" style="top:471px">
    <h3>OUR CATEGORIES</h3>
    <ul style="margin-top:9px">
      <li>Rings<span class="plus">+</span></li>
      <li>Bracelets<span class="plus">+</span></li>
      <li>Earrings<span class="plus">+</span></li>
      <li>Necklaces</li><li>Estate</li><li>Watches</li><li>Men's</li><li>Children's</li>
    </ul>
  </div>

  <div class="side" style="top:785px">
    <h3>OUR VENDORS</h3>
    <ul style="margin-top:9px">
      <li><span><i class="box"></i>Vendor</span><span class="count">1</span></li>
      <li><span><i class="box"></i>Vendor</span><span class="count">10</span></li>
      <li><span><i class="box"></i>Vendor</span><span class="count">11</span></li>
      <li><span><i class="box"></i>Vendor</span><span class="count">12</span></li>
      <li><span><i class="box"></i>Vendor</span><span class="count">2</span></li>
    </ul>
  </div>

  <div class="side" style="top:1006px">
    <h3>PRODUCTS TYPES</h3>
    <ul style="margin-top:9px">
      <li><span><i class="box"></i>Type</span><span class="count">1</span></li>
      <li><span><i class="box"></i>Type</span><span class="count">10</span></li>
      <li><span><i class="box"></i>Type</span><span class="count">11</span></li>
      <li><span><i class="box"></i>Type</span><span class="count">12</span></li>
      <li><span><i class="box"></i>Type</span><span class="count">2</span></li>
    </ul>
  </div>

  <div class="side" style="top:1231px">
    <h3>COLOURS</h3>
    <div class="swatches"><span style="background:#888"></span><span style="background:#000"></span><span style="background:#0a0aa0"></span><span style="background:#ffd800"></span><span style="background:#a00000"></span></div>
  </div>

  <div class="side" style="top:1345px">
    <h3>SIZES</h3>
    <ul style="margin-top:9px">
      <li><span><i class="box"></i>Small</span></li>
      <li><span><i class="box"></i>Medium</span></li>
      <li><span><i class="box"></i>Learge</span></li>
      <li><span><i class="box"></i>Xl</span></li>
      <li><span><i class="box"></i>Xxl</span></li>
    </ul>
  </div>

  <div class="side" style="top:1570px">
    <h3>TAGS</h3>
    <div class="tags">
      <div class="tagrow"><span>BLACK</span><span>BLUE</span><span>FIBER</span></div>
      <div class="tagrow"><span>GOLD</span><span>GREY</span><span>GREEN</span><span>L</span></div>
      <div class="tagrow"><span>LEATHER</span><span>M</span><span>MAGENTA</span></div>
      <div class="tagrow"><span>MAROON</span><span>METAL</span><span>NAVY</span></div>
      <div class="tagrow"><span>ORANGE</span><span>PINK</span></div>
    </div>
  </div>
</aside>

<main>
  <div class="toolbar">
    <div class="views">
      <svg width="18" height="16" viewBox="0 0 18 16" fill="#d8ac2c"><rect x="0" y="0" width="5" height="4"/><rect x="6.5" y="0" width="5" height="4"/><rect x="13" y="0" width="5" height="4"/><rect x="0" y="6" width="5" height="4"/><rect x="6.5" y="6" width="5" height="4"/><rect x="13" y="6" width="5" height="4"/><rect x="0" y="12" width="5" height="4"/><rect x="6.5" y="12" width="5" height="4"/><rect x="13" y="12" width="5" height="4"/></svg>
      <svg width="19" height="16" viewBox="0 0 19 16" fill="#999"><rect x="0" y="0" width="4" height="3"/><rect x="6" y="0" width="13" height="3"/><rect x="0" y="6.5" width="4" height="3"/><rect x="6" y="6.5" width="13" height="3"/><rect x="0" y="13" width="4" height="3"/><rect x="6" y="13" width="13" height="3"/></svg>
    </div>
    <div class="count">Showing 1 - 15 Of 34 Result</div>
    <div class="sortlabel">Sort by:</div>
    <div class="select"><span>All product..</span><i><svg width="10" height="7" viewBox="0 0 10 7"><path d="M1 1l4 4 4-4" fill="none" stroke="#000" stroke-width="1.6"/></svg></i></div>
  </div>

  <div class="grid">
    <article class="card"><div class="photo gold-photo" role="img" aria-label="Gold disc pendant with diamond initial"></div><div class="stars"><svg viewBox="0 0 20 20"><path d="M10 1l2.7 6 6.3.6-4.8 4.3 1.4 6.4L10 15l-5.6 3.3 1.4-6.4L1 7.6 7.3 7z"/></svg><svg viewBox="0 0 20 20"><path d="M10 1l2.7 6 6.3.6-4.8 4.3 1.4 6.4L10 15l-5.6 3.3 1.4-6.4L1 7.6 7.3 7z"/></svg><svg viewBox="0 0 20 20"><path d="M10 1l2.7 6 6.3.6-4.8 4.3 1.4 6.4L10 15l-5.6 3.3 1.4-6.4L1 7.6 7.3 7z"/></svg><svg viewBox="0 0 20 20"><path d="M10 1l2.7 6 6.3.6-4.8 4.3 1.4 6.4L10 15l-5.6 3.3 1.4-6.4L1 7.6 7.3 7z"/></svg><svg viewBox="0 0 20 20"><path d="M10 1l2.7 6 6.3.6-4.8 4.3 1.4 6.4L10 15l-5.6 3.3 1.4-6.4L1 7.6 7.3 7z"/></svg></div><h4>PRODUCT HEADING</h4><div class="price">$10.00</div></article>

    <article class="card is-active"><div class="photo mixed-photo" role="img" aria-label="Stacked gold, silver and black beaded bangles" style="height:170px"></div><div class="stars"><svg viewBox="0 0 20 20"><path d="M10 1l2.7 6 6.3.6-4.8 4.3 1.4 6.4L10 15l-5.6 3.3 1.4-6.4L1 7.6 7.3 7z"/></svg><svg viewBox="0 0 20 20"><path d="M10 1l2.7 6 6.3.6-4.8 4.3 1.4 6.4L10 15l-5.6 3.3 1.4-6.4L1 7.6 7.3 7z"/></svg><svg viewBox="0 0 20 20"><path d="M10 1l2.7 6 6.3.6-4.8 4.3 1.4 6.4L10 15l-5.6 3.3 1.4-6.4L1 7.6 7.3 7z"/></svg><svg viewBox="0 0 20 20"><path d="M10 1l2.7 6 6.3.6-4.8 4.3 1.4 6.4L10 15l-5.6 3.3 1.4-6.4L1 7.6 7.3 7z"/></svg><svg viewBox="0 0 20 20"><path d="M10 1l2.7 6 6.3.6-4.8 4.3 1.4 6.4L10 15l-5.6 3.3 1.4-6.4L1 7.6 7.3 7z"/></svg></div><h4>PRODUCT HEADING</h4><div class="price">$10.00</div>
      <div class="actions"><span class="add">ADD TO CART</span>
        <span class="ic"><svg viewBox="0 0 24 24"><circle cx="10" cy="10" r="7" fill="none" stroke="#fff" stroke-width="3"/><path d="M15 15l7 7" stroke="#fff" stroke-width="3"/></svg></span>
        <span class="ic"><svg viewBox="0 0 24 24"><path d="M12 21l-8-8a5 5 0 017-7l1 1 1-1a5 5 0 017 7z" fill="#fff"/></svg></span>
        <span class="ic"><svg viewBox="0 0 24 24"><path d="M10 14l4-4M8 11l-3 3a4 4 0 006 6l3-3M16 13l3-3a4 4 0 00-6-6l-3 3" fill="none" stroke="#fff" stroke-width="2.5"/></svg></span>
      </div>
    </article>

    <article class="card"><div class="photo mixed-photo" role="img" aria-label="Gold and silver coil bracelets"></div><div class="stars"><svg viewBox="0 0 20 20"><path d="M10 1l2.7 6 6.3.6-4.8 4.3 1.4 6.4L10 15l-5.6 3.3 1.4-6.4L1 7.6 7.3 7z"/></svg><svg viewBox="0 0 20 20"><path d="M10 1l2.7 6 6.3.6-4.8 4.3 1.4 6.4L10 15l-5.6 3.3 1.4-6.4L1 7.6 7.3 7z"/></svg><svg viewBox="0 0 20 20"><path d="M10 1l2.7 6 6.3.6-4.8 4.3 1.4 6.4L10 15l-5.6 3.3 1.4-6.4L1 7.6 7.3 7z"/></svg><svg viewBox="0 0 20 20"><path d="M10 1l2.7 6 6.3.6-4.8 4.3 1.4 6.4L10 15l-5.6 3.3 1.4-6.4L1 7.6 7.3 7z"/></svg><svg viewBox="0 0 20 20"><path d="M10 1l2.7 6 6.3.6-4.8 4.3 1.4 6.4L10 15l-5.6 3.3 1.4-6.4L1 7.6 7.3 7z"/></svg></div><h4>PRODUCT HEADING</h4><div class="price">$10.00</div></article>

    <article class="card"><div class="photo silver-photo" role="img" aria-label="Diamond drop earrings"></div><div class="stars"><svg viewBox="0 0 20 20"><path d="M10 1l2.7 6 6.3.6-4.8 4.3 1.4 6.4L10 15l-5.6 3.3 1.4-6.4L1 7.6 7.3 7z"/></svg><svg viewBox="0 0 20 20"><path d="M10 1l2.7 6 6.3.6-4.8 4.3 1.4 6.4L10 15l-5.6 3.3 1.4-6.4L1 7.6 7.3 7z"/></svg><svg viewBox="0 0 20 20"><path d="M10 1l2.7 6 6.3.6-4.8 4.3 1.4 6.4L10 15l-5.6 3.3 1.4-6.4L1 7.6 7.3 7z"/></svg><svg viewBox="0 0 20 20"><path d="M10 1l2.7 6 6.3.6-4.8 4.3 1.4 6.4L10 15l-5.6 3.3 1.4-6.4L1 7.6 7.3 7z"/></svg><svg viewBox="0 0 20 20"><path d="M10 1l2.7 6 6.3.6-4.8 4.3 1.4 6.4L10 15l-5.6 3.3 1.4-6.4L1 7.6 7.3 7z"/></svg></div><h4>PRODUCT HEADING</h4><div class="price">$10.00</div></article>

    <article class="card"><div class="photo silver-photo" role="img" aria-label="Diamond solitaire pendant on gold chain" style="background:radial-gradient(ellipse at 50% 55%,#f1f3f5 0,#d8c27a 35%,#fff 70%)"></div><div class="stars"><svg viewBox="0 0 20 20"><path d="M10 1l2.7 6 6.3.6-4.8 4.3 1.4 6.4L10 15l-5.6 3.3 1.4-6.4L1 7.6 7.3 7z"/></svg><svg viewBox="0 0 20 20"><path d="M10 1l2.7 6 6.3.6-4.8 4.3 1.4 6.4L10 15l-5.6 3.3 1.4-6.4L1 7.6 7.3 7z"/></svg><svg viewBox="0 0 20 20"><path d="M10 1l2.7 6 6.3.6-4.8 4.3 1.4 6.4L10 15l-5.6 3.3 1.4-6.4L1 7.6 7.3 7z"/></svg><svg viewBox="0 0 20 20"><path d="M10 1l2.7 6 6.3.6-4.8 4.3 1.4 6.4L10 15l-5.6 3.3 1.4-6.4L1 7.6 7.3 7z"/></svg><svg viewBox="0 0 20 20"><path d="M10 1l2.7 6 6.3.6-4.8 4.3 1.4 6.4L10 15l-5.6 3.3 1.4-6.4L1 7.6 7.3 7z"/></svg></div><h4>PRODUCT HEADING</h4><div class="price">$10.00</div></article>

    <article class="card"><div class="photo silver-photo" role="img" aria-label="Diamond halo engagement ring"></div><div class="stars"><svg viewBox="0 0 20 20"><path d="M10 1l2.7 6 6.3.6-4.8 4.3 1.4 6.4L10 15l-5.6 3.3 1.4-6.4L1 7.6 7.3 7z"/></svg><svg viewBox="0 0 20 20"><path d="M10 1l2.7 6 6.3.6-4.8 4.3 1.4 6.4L10 15l-5.6 3.3 1.4-6.4L1 7.6 7.3 7z"/></svg><svg viewBox="0 0 20 20"><path d="M10 1l2.7 6 6.3.6-4.8 4.3 1.4 6.4L10 15l-5.6 3.3 1.4-6.4L1 7.6 7.3 7z"/></svg><svg viewBox="0 0 20 20"><path d="M10 1l2.7 6 6.3.6-4.8 4.3 1.4 6.4L10 15l-5.6 3.3 1.4-6.4L1 7.6 7.3 7z"/></svg><svg viewBox="0 0 20 20"><path d="M10 1l2.7 6 6.3.6-4.8 4.3 1.4 6.4L10 15l-5.6 3.3 1.4-6.4L1 7.6 7.3 7z"/></svg></div><h4>PRODUCT HEADING</h4><div class="price">$10.00</div></article>

    <article class="card"><div class="photo silver-photo" role="img" aria-label="Emerald-cut diamond ring"></div><div class="stars"><svg viewBox="0 0 20 20"><path d="M10 1l2.7 6 6.3.6-4.8 4.3 1.4 6.4L10 15l-5.6 3.3 1.4-6.4L1 7.6 7.3 7z"/></svg><svg viewBox="0 0 20 20"><path d="M10 1l2.7 6 6.3.6-4.8 4.3 1.4 6.4L10 15l-5.6 3.3 1.4-6.4L1 7.6 7.3 7z"/></svg><svg viewBox="0 0 20 20"><path d="M10 1l2.7 6 6.3.6-4.8 4.3 1.4 6.4L10 15l-5.6 3.3 1.4-6.4L1 7.6 7.3 7z"/></svg><svg viewBox="0 0 20 20"><path d="M10 1l2.7 6 6.3.6-4.8 4.3 1.4 6.4L10 15l-5.6 3.3 1.4-6.4L1 7.6 7.3 7z"/></svg><svg viewBox="0 0 20 20"><path d="M10 1l2.7 6 6.3.6-4.8 4.3 1.4 6.4L10 15l-5.6 3.3 1.4-6.4L1 7.6 7.3 7z"/></svg></div><h4>PRODUCT HEADING</h4><div class="price">$10.00</div></article>

    <article class="card"><div class="photo pearl-photo" role="img" aria-label="Pearl stud earrings"></div><div class="stars"><svg viewBox="0 0 20 20"><path d="M10 1l2.7 6 6.3.6-4.8 4.3 1.4 6.4L10 15l-5.6 3.3 1.4-6.4L1 7.6 7.3 7z"/></svg><svg viewBox="0 0 20 20"><path d="M10 1l2.7 6 6.3.6-4.8 4.3 1.4 6.4L10 15l-5.6 3.3 1.4-6.4L1 7.6 7.3 7z"/></svg><svg viewBox="0 0 20 20"><path d="M10 1l2.7 6 6.3.6-4.8 4.3 1.4 6.4L10 15l-5.6 3.3 1.4-6.4L1 7.6 7.3 7z"/></svg><svg viewBox="0 0 20 20"><path d="M10 1l2.7 6 6.3.6-4.8 4.3 1.4 6.4L10 15l-5.6 3.3 1.4-6.4L1 7.6 7.3 7z"/></svg><svg viewBox="0 0 20 20"><path d="M10 1l2.7 6 6.3.6-4.8 4.3 1.4 6.4L10 15l-5.6 3.3 1.4-6.4L1 7.6 7.3 7z"/></svg></div><h4>PRODUCT HEADING</h4><div class="price">$10.00</div></article>

    <article class="card"><div class="photo silver-photo" role="img" aria-label="Cushion halo diamond ring"></div><div class="stars"><svg viewBox="0 0 20 20"><path d="M10 1l2.7 6 6.3.6-4.8 4.3 1.4 6.4L10 15l-5.6 3.3 1.4-6.4L1 7.6 7.3 7z"/></svg><svg viewBox="0 0 20 20"><path d="M10 1l2.7 6 6.3.6-4.8 4.3 1.4 6.4L10 15l-5.6 3.3 1.4-6.4L1 7.6 7.3 7z"/></svg><svg viewBox="0 0 20 20"><path d="M10 1l2.7 6 6.3.6-4.8 4.3 1.4 6.4L10 15l-5.6 3.3 1.4-6.4L1 7.6 7.3 7z"/></svg><svg viewBox="0 0 20 20"><path d="M10 1l2.7 6 6.3.6-4.8 4.3 1.4 6.4L10 15l-5.6 3.3 1.4-6.4L1 7.6 7.3 7z"/></svg><svg viewBox="0 0 20 20"><path d="M10 1l2.7 6 6.3.6-4.8 4.3 1.4 6.4L10 15l-5.6 3.3 1.4-6.4L1 7.6 7.3 7z"/></svg></div><h4>PRODUCT HEADING</h4><div class="price">$10.00</div></article>

    <article class="card"><div class="photo silver-photo" role="img" aria-label="Black and white diamond coil bracelet" style="background:radial-gradient(ellipse at 50% 50%,#9a9a9a 0,#d6d6d6 40%,#fff 72%)"></div><div class="stars"><svg viewBox="0 0 20 20"><path d="M10 1l2.7 6 6.3.6-4.8 4.3 1.4 6.4L10 15l-5.6 3.3 1.4-6.4L1 7.6 7.3 7z"/></svg><svg viewBox="0 0 20 20"><path d="M10 1l2.7 6 6.3.6-4.8 4.3 1.4 6.4L10 15l-5.6 3.3 1.4-6.4L1 7.6 7.3 7z"/></svg><svg viewBox="0 0 20 20"><path d="M10 1l2.7 6 6.3.6-4.8 4.3 1.4 6.4L10 15l-5.6 3.3 1.4-6.4L1 7.6 7.3 7z"/></svg><svg viewBox="0 0 20 20"><path d="M10 1l2.7 6 6.3.6-4.8 4.3 1.4 6.4L10 15l-5.6 3.3 1.4-6.4L1 7.6 7.3 7z"/></svg><svg viewBox="0 0 20 20"><path d="M10 1l2.7 6 6.3.6-4.8 4.3 1.4 6.4L10 15l-5.6 3.3 1.4-6.4L1 7.6 7.3 7z"/></svg></div><h4>PRODUCT HEADING</h4><div class="price">$10.00</div></article>

    <article class="card"><div class="photo silver-photo" role="img" aria-label="Diamond cross pendant on chain"></div><div class="stars"><svg viewBox="0 0 20 20"><path d="M10 1l2.7 6 6.3.6-4.8 4.3 1.4 6.4L10 15l-5.6 3.3 1.4-6.4L1 7.6 7.3 7z"/></svg><svg viewBox="0 0 20 20"><path d="M10 1l2.7 6 6.3.6-4.8 4.3 1.4 6.4L10 15l-5.6 3.3 1.4-6.4L1 7.6 7.3 7z"/></svg><svg viewBox="0 0 20 20"><path d="M10 1l2.7 6 6.3.6-4.8 4.3 1.4 6.4L10 15l-5.6 3.3 1.4-6.4L1 7.6 7.3 7z"/></svg><svg viewBox="0 0 20 20"><path d="M10 1l2.7 6 6.3.6-4.8 4.3 1.4 6.4L10 15l-5.6 3.3 1.4-6.4L1 7.6 7.3 7z"/></svg><svg viewBox="0 0 20 20"><path d="M10 1l2.7 6 6.3.6-4.8 4.3 1.4 6.4L10 15l-5.6 3.3 1.4-6.4L1 7.6 7.3 7z"/></svg></div><h4>PRODUCT HEADING</h4><div class="price">$10.00</div></article>

    <article class="card"><div class="photo gold-photo" role="img" aria-label="Gold disc pendant with diamond initial"></div><div class="stars"><svg viewBox="0 0 20 20"><path d="M10 1l2.7 6 6.3.6-4.8 4.3 1.4 6.4L10 15l-5.6 3.3 1.4-6.4L1 7.6 7.3 7z"/></svg><svg viewBox="0 0 20 20"><path d="M10 1l2.7 6 6.3.6-4.8 4.3 1.4 6.4L10 15l-5.6 3.3 1.4-6.4L1 7.6 7.3 7z"/></svg><svg viewBox="0 0 20 20"><path d="M10 1l2.7 6 6.3.6-4.8 4.3 1.4 6.4L10 15l-5.6 3.3 1.4-6.4L1 7.6 7.3 7z"/></svg><svg viewBox="0 0 20 20"><path d="M10 1l2.7 6 6.3.6-4.8 4.3 1.4 6.4L10 15l-5.6 3.3 1.4-6.4L1 7.6 7.3 7z"/></svg><svg viewBox="0 0 20 20"><path d="M10 1l2.7 6 6.3.6-4.8 4.3 1.4 6.4L10 15l-5.6 3.3 1.4-6.4L1 7.6 7.3 7z"/></svg></div><h4>PRODUCT HEADING</h4><div class="price">$10.00</div></article>

    <article class="card"><div class="photo silver-photo" role="img" aria-label="Diamond halo engagement ring"></div><div class="stars"><svg viewBox="0 0 20 20"><path d="M10 1l2.7 6 6.3.6-4.8 4.3 1.4 6.4L10 15l-5.6 3.3 1.4-6.4L1 7.6 7.3 7z"/></svg><svg viewBox="0 0 20 20"><path d="M10 1l2.7 6 6.3.6-4.8 4.3 1.4 6.4L10 15l-5.6 3.3 1.4-6.4L1 7.6 7.3 7z"/></svg><svg viewBox="0 0 20 20"><path d="M10 1l2.7 6 6.3.6-4.8 4.3 1.4 6.4L10 15l-5.6 3.3 1.4-6.4L1 7.6 7.3 7z"/></svg><svg viewBox="0 0 20 20"><path d="M10 1l2.7 6 6.3.6-4.8 4.3 1.4 6.4L10 15l-5.6 3.3 1.4-6.4L1 7.6 7.3 7z"/></svg><svg viewBox="0 0 20 20"><path d="M10 1l2.7 6 6.3.6-4.8 4.3 1.4 6.4L10 15l-5.6 3.3 1.4-6.4L1 7.6 7.3 7z"/></svg></div><h4>PRODUCT HEADING</h4><div class="price">$10.00</div></article>

    <article class="card"><div class="photo color-photo" role="img" aria-label="Multicolour enamel hoop earrings"></div><div class="stars"><svg viewBox="0 0 20 20"><path d="M10 1l2.7 6 6.3.6-4.8 4.3 1.4 6.4L10 15l-5.6 3.3 1.4-6.4L1 7.6 7.3 7z"/></svg><svg viewBox="0 0 20 20"><path d="M10 1l2.7 6 6.3.6-4.8 4.3 1.4 6.4L10 15l-5.6 3.3 1.4-6.4L1 7.6 7.3 7z"/></svg><svg viewBox="0 0 20 20"><path d="M10 1l2.7 6 6.3.6-4.8 4.3 1.4 6.4L10 15l-5.6 3.3 1.4-6.4L1 7.6 7.3 7z"/></svg><svg viewBox="0 0 20 20"><path d="M10 1l2.7 6 6.3.6-4.8 4.3 1.4 6.4L10 15l-5.6 3.3 1.4-6.4L1 7.6 7.3 7z"/></svg><svg viewBox="0 0 20 20"><path d="M10 1l2.7 6 6.3.6-4.8 4.3 1.4 6.4L10 15l-5.6 3.3 1.4-6.4L1 7.6 7.3 7z"/></svg></div><h4>PRODUCT HEADING</h4><div class="price">$10.00</div></article>

    <article class="card"><div class="photo color-photo" role="img" aria-label="Multicolour enamel dome ring"></div><div class="stars"><svg viewBox="0 0 20 20"><path d="M10 1l2.7 6 6.3.6-4.8 4.3 1.4 6.4L10 15l-5.6 3.3 1.4-6.4L1 7.6 7.3 7z"/></svg><svg viewBox="0 0 20 20"><path d="M10 1l2.7 6 6.3.6-4.8 4.3 1.4 6.4L10 15l-5.6 3.3 1.4-6.4L1 7.6 7.3 7z"/></svg><svg viewBox="0 0 20 20"><path d="M10 1l2.7 6 6.3.6-4.8 4.3 1.4 6.4L10 15l-5.6 3.3 1.4-6.4L1 7.6 7.3 7z"/></svg><svg viewBox="0 0 20 20"><path d="M10 1l2.7 6 6.3.6-4.8 4.3 1.4 6.4L10 15l-5.6 3.3 1.4-6.4L1 7.6 7.3 7z"/></svg><svg viewBox="0 0 20 20"><path d="M10 1l2.7 6 6.3.6-4.8 4.3 1.4 6.4L10 15l-5.6 3.3 1.4-6.4L1 7.6 7.3 7z"/></svg></div><h4>PRODUCT HEADING</h4><div class="price">$10.00</div></article>
  </div>

  <div class="pager">
    <span class="prev">‹&nbsp; Prev</span>
    <span class="num" style="left:669px">1</span>
    <span class="on">2</span>
    <span class="num" style="left:746px">3</span>
    <span class="num" style="left:774px">...</span>
    <span class="num" style="left:800px">82</span>
    <span class="next">Next &nbsp;›</span>
  </div>
</main>

<footer class="footer">
  <h2>NEWSLETTER</h2>
  <div class="signup">
    <div class="field"><svg width="18" height="13" viewBox="0 0 18 13"><rect width="18" height="13" rx="1" fill="#bbb"/><path d="M0 1l9 6 9-6" fill="none" stroke="#fff" stroke-width="1.4"/></svg>Enter your email address</div>
    <div class="btn">SUBSCRIBE</div>
  </div>

  <div class="fbrand">Brill's Jewelers</div>
  <div class="social"><span style="background:#3b5998"></span><span style="background:#1da1f2"></span><span style="background:#dd4b39"></span></div>

  <div class="fcol" style="left:389px"><h5>Information</h5><p style="margin-top:-2px">My account<br>Wishlist<br>Checkout<br>Cart<br>Contact</p></div>
  <div class="fcol" style="left:549px"><h5>Quick links</h5><p style="margin-top:-11px">Home<br>About<br>Jewelry<br>Diamonds<br>Services</p></div>
  <div class="fcol" style="left:706px"><h5>Support</h5><p style="margin-top:-2px">Terms of use<br>Terms and Conditions<br>Privacy Policy<br>Returns<br>Refunds.</p></div>
  <div class="fcol contact" style="left:889px;width:250px"><h5>Contact Us</h5>
    <p><svg viewBox="0 0 24 24"><path d="M6 2l4 4-2 3a12 12 0 007 7l3-2 4 4-3 4C10 22 2 14 2 5z" fill="#fff"/></svg>(305)555-0142</p>
    <p><svg viewBox="0 0 24 18"><rect width="24" height="18" fill="#fff"/><path d="M0 1l12 8 12-8" fill="none" stroke="#000" stroke-width="2"/></svg><span class="mail">hello@brillsjewelers-example.com</span></p>
    <p><svg viewBox="0 0 24 24"><path d="M12 1a8 8 0 00-8 8c0 6 8 14 8 14s8-8 8-14a8 8 0 00-8-8zm0 11a3 3 0 110-6 3 3 0 010 6z" fill="#fff"/></svg>418 Palm Vista Ave, Seabright, FL 33990</p>
  </div>

  <div class="fline"></div>
  <div class="copy">© Copyright 2020 All Right Reserved</div>
  <div class="pay"><span></span><span></span><span></span></div>
</footer>

<div class="chat"><svg width="24" height="22" viewBox="0 0 24 22"><path d="M12 1C6 1 1 5 1 10c0 3 2 5 4 7l-1 4 5-2c1 .3 2 .4 3 .4 6 0 11-4 11-9.4S18 1 12 1z" fill="#000"/><circle cx="7.5" cy="10" r="1.5" fill="#fff"/><circle cx="12" cy="10" r="1.5" fill="#fff"/><circle cx="16.5" cy="10" r="1.5" fill="#fff"/></svg></div>

</body>
</html>
```